Construction Company's Job Site Signage City ordinance job signage for brand awareness.

We are looking for something with movement or texture (ei. water or something like that) and dislikes a white background. We are a company specializing in remedial construction, mold removal, and restoration. The concept is for 12” x 18” jobsite signs so they must be easy to read from a passing car as well. Please let me know if there is anything I can do to help or if it’s easier for me to submit. The CGC Number must be at least 1 inch lettering. www.BrookvaleGroup.com

Target Market(s)

Upscale, high end estate neighborhoods at job sites which we are working on.

Industry/Entity Type

Construction

Colors
33b8a4
00a990
0892cd
0255a3
9bcb3c
add136
fbed22
fbee3e
fbf289

Requirements
Must have
• All text present in the current files.

```html
<!DOCTYPE html>
<html lang="en">
<head>
<meta charset="utf-8">
<title>Brookvale Group – Job Site Sign</title>
<link rel="stylesheet" href="https://fonts.googleapis.com/css2?family=Anton&display=swap">
<style>
  :root {
    --page: #f2f3f0;
    --forest: #0b4524;
    --leaf-light: #e9f5c8;
    --leaf: #9bcb3c;
    --leaf-mid: #6fb72e;
    --grass: #3f8f1c;
    --grass-deep: #2c6f12;
    --band: rgba(22, 92, 24, 0.88);
    --yellow: #fbed22;
    --white: #ffffff;
  }
  * { margin: 0; padding: 0; box-sizing: border-box; }
  html, body {
    width: 1200px;
    height: 1071px;
    overflow: hidden;
    background: var(--page);
  }
  .sign {
    position: absolute;
    left: 45px;
    top: 165px;
    width: 1110px;
    height: 740px;
    overflow: hidden;
    font-family: "Anton", "Arial Narrow", sans-serif;
    box-shadow: 0 6px 18px rgba(0,0,0,0.18);
  }
  .sign__backdrop {
    position: absolute;
    inset: 0;
    background:
      radial-gradient(ellipse 420px 300px at 300px 60px, rgba(255,255,255,0.95), rgba(255,255,255,0) 70%),
      radial-gradient(ellipse 600px 380px at 800px 220px, rgba(200,230,60,0.55), rgba(200,230,60,0) 70%),
      linear-gradient(180deg, var(--leaf-light) 0%, var(--leaf) 35%, var(--leaf-mid) 58%, var(--grass) 72%, var(--grass-deep) 100%);
  }
  .brand {
    position: absolute;
    left: 40px;
    top: 62px;
    display: flex;
    align-items: center;
    gap: 16px;
    color: var(--forest);
  }
  .brand__mark {
    width: 58px;
    height: 58px;
    background: var(--forest);
  }
  .brand__name {
    font-size: 74px;
    line-height: 1;
    letter-spacing: 1px;
  }
  .tagline {
    position: absolute;
    left: 0;
    right: 0;
    top: 318px;
    text-align: center;
    color: var(--forest);
    font-size: 66px;
    line-height: 96px;
    letter-spacing: 1px;
    text-shadow:
      3px 0 0 var(--white), -3px 0 0 var(--white),
      0 3px 0 var(--white), 0 -3px 0 var(--white),
      2px 2px 0 var(--white), -2px -2px 0 var(--white),
      2px -2px 0 var(--white), -2px 2px 0 var(--white);
  }
  .contact-band {
    position: absolute;
    left: 0;
    right: 0;
    top: 605px;
    height: 106px;
    background: var(--band);
    display: flex;
    align-items: center;
    justify-content: center;
    gap: 34px;
    color: var(--yellow);
    font-size: 70px;
    letter-spacing: 1px;
  }
  .contact-band__divider {
    width: 4px;
    height: 38px;
    background: var(--yellow);
  }
</style>
</head>
<body>
  <main class="sign">
    <div class="sign__backdrop" role="img" aria-label="Sunlit green lawn with soft bokeh light in the background"></div>

    <div class="brand">
      <span class="brand__mark"></span>
      <span class="brand__name">BROOKVALE GROUP</span>
    </div>

    <p class="tagline">-BUILDING SOLUTIONS<br>AROUND COMPLEX STRUCTURES-</p>

    <div class="contact-band">
      <span class="contact-band__phone">(239) 555-0148</span>
      <span class="contact-band__divider"></span>
      <span class="contact-band__license">CGC 1528034</span>
    </div>
  </main>
</body>
</html>
```